A Maple Syrup Label for a Local Buniness

We are looking for a label for our maple syrup business. Our business currently sells honey, and we are expanding into maple syrup. Our Business name is "Corvale Bees" and we currently have a logo attached below. We would like to incorporate the bee and CB part, but the label could also read "Corvale Farms" with the words maple syrup. We do not want consumers to confuse the maple syrup jars with the honey jars. It should be clear that the jars contain maple syrup. We are open to new designs as well.

```html
<!DOCTYPE html>
<html lang="en">
<head>
<meta charset="utf-8">
<title>Corvale Farms Maple Syrup Label</title>
<link href="https://fonts.googleapis.com/css2?family=Montserrat:wght@600&family=Libre+Baskerville&family=Oswald:wght@700&family=Poppins:wght@400&family=Open+Sans:wght@400&display=swap" rel="stylesheet">
<style>
  :root {
    --page: #ffffff;
    --label-edge: #fbe3d2;
    --label-ring: #f9bd10;
    --label-cream-top: #ffffff;
    --label-cream-bottom: #fdebd8;
    --ink: #111111;
    --band-dark: #0b0b0b;
    --band-text: #ffffff;
  }
  html, body {
    margin: 0;
    padding: 0;
    background: var(--page);
    overflow: hidden;
  }
  .canvas {
    width: 1200px;
    height: 993px;
    overflow: hidden;
    background: var(--page);
  }
  .label { display: block; width: 1200px; height: 993px; }
  .label__edge { fill: var(--label-edge); }
  .label__ring { fill: var(--label-ring); }
  .label__farm-name {
    font-family: "Montserrat", sans-serif;
    font-weight: 600;
    font-size: 40px;
    letter-spacing: 3px;
    fill: var(--ink);
  }
  .label__brand {
    font-family: "Libre Baskerville", serif;
    font-size: 46px;
    fill: var(--ink);
  }
  .label__brand-dot { fill: var(--label-ring); }
  .label__band { fill: var(--label-ring); }
  .label__product {
    font-family: "Oswald", sans-serif;
    font-weight: 700;
    font-size: 90px;
    fill: var(--ink);
  }
  .label__volume-band { fill: var(--band-dark); }
  .label__volume {
    font-family: "Poppins", sans-serif;
    font-size: 46px;
    fill: var(--band-text);
  }
  .label__volume-mark { fill: var(--label-ring); }
  .label__purity {
    font-family: "Open Sans", sans-serif;
    font-size: 28px;
    fill: var(--ink);
  }
</style>
</head>
<body>
<main class="canvas">
  <svg class="label" viewBox="0 0 1200 993" xmlns="http://www.w3.org/2000/svg">
    <defs>
      <linearGradient id="cream-fill" x1="0" y1="0" x2="0" y2="1">
        <stop offset="0" stop-color="var(--label-cream-top)"/>
        <stop offset="1" stop-color="var(--label-cream-bottom)"/>
      </linearGradient>
      <clipPath id="label-inner">
        <ellipse cx="600" cy="496" rx="307" ry="399"/>
      </clipPath>
      <path id="farm-arc" d="M 372 424 A 228 228 0 0 1 828 424"/>
    </defs>

    <ellipse class="label__edge" cx="600" cy="496" rx="345" ry="447"/>
    <ellipse class="label__ring" cx="600" cy="496" rx="327" ry="423"/>
    <ellipse cx="600" cy="496" rx="307" ry="399" fill="url(#cream-fill)"/>

    <text class="label__farm-name" text-anchor="middle">
      <textPath href="#farm-arc" startOffset="50%">CORVALE FARMS</textPath>
    </text>

    <circle class="label__brand-dot" cx="600" cy="338" r="22"/>
    <text class="label__brand" x="600" y="430" text-anchor="middle">CORVALE</text>
    <text class="label__brand" x="600" y="488" text-anchor="middle">BEES</text>

    <g clip-path="url(#label-inner)">
      <rect class="label__band" x="250" y="608" width="700" height="128"/>
      <rect class="label__volume-band" x="250" y="733" width="700" height="72"/>
    </g>

    <text class="label__product" x="603" y="703" text-anchor="middle">MAPLE SYRUP</text>

    <g class="label__volume-mark">
      <circle cx="430" cy="770" r="8"/>
      <circle cx="462" cy="770" r="8"/>
      <circle cx="494" cy="770" r="8"/>
      <circle cx="706" cy="770" r="8"/>
      <circle cx="738" cy="770" r="8"/>
      <circle cx="770" cy="770" r="8"/>
    </g>
    <text class="label__volume" x="600" y="786" text-anchor="middle">250ml</text>

    <text class="label__purity" x="602" y="852" text-anchor="middle">100% PURE</text>
  </svg>
</main>
</body>
</html>
```